Email template for construction companies

Hello, I'm looking to build out an html email template for our email marketing. I'd like it to compliment our website, but not be an exact replication of it.

This template will be used in all of our email marketing campaigns. We provide financial support for construction companies, so it needs to express stability and confidence, but not the stuffiness of a traditional bank.

Target Market(s)

Construction companies (subcontractors specifically)

Industry/Entity Type

Construction Company

Font styles to use
Serif

Requirements
Must have
• Must compliment our website, but not be a replica.
Should not have
• Should not be an exact replica of our website.

```html
<!DOCTYPE html>
<html lang="en">
<head>
<meta charset="utf-8">
<title>BuildLedger – Funding the Construction Industry</title>
<link href="https://fonts.googleapis.com/css2?family=Roboto:wght@300;400;500;700&display=swap" rel="stylesheet">
<style>
:root{
  --charcoal:#2b2d31;
  --charcoal-deep:#222427;
  --charcoal-line:#3a3d42;
  --orange:#f26b1d;
  --white:#ffffff;
  --text:#3b3b3b;
  --muted:#6b6b6b;
  --panel:#f3f3f3;
  --rule:#dcdcdc;
}
*{box-sizing:border-box;margin:0;padding:0}
html,body{width:882px;height:1200px;overflow:hidden;background:var(--white)}
body{font-family:"Roboto",Arial,sans-serif;color:var(--text);position:relative}
.email{position:absolute;inset:0}

.topbar{position:absolute;left:0;top:0;width:882px;height:78px;background:var(--charcoal);border-bottom:1px solid var(--charcoal-line);display:flex;align-items:center;padding-left:40px}
.brand{display:flex;align-items:center;gap:12px;color:var(--white);font-size:28px;font-weight:500}
.brand-dot{width:30px;height:30px;border-radius:50%;background:var(--white)}

.hero{position:absolute;left:0;top:78px;width:882px;height:332px;background:var(--charcoal)}
.hero-title{position:absolute;left:40px;top:80px;font-weight:300;font-size:54px;line-height:1.12;color:var(--white)}
.hero-title .accent{color:var(--orange);font-weight:500}
.hero-title strong{font-weight:700}
.hero-visual{position:absolute;left:535px;top:20px;width:310px;height:290px}
.hero-circle{position:absolute;left:20px;top:40px;width:250px;height:250px;border-radius:50%;background:var(--orange)}
.hero-art{position:absolute;left:55px;top:10px;width:240px;height:250px;border-radius:6px;background:linear-gradient(160deg,#3f8ec4,#2a4f7a 55%,#e1a23f)}

.spotlight{position:absolute;left:40px;top:426px;width:505px}
.spotlight h2{font-size:22px;font-weight:700;color:var(--charcoal);margin-bottom:4px;line-height:1.2}
.spotlight p{font-size:13.5px;line-height:1.32;color:var(--text);margin-bottom:12px;text-align:justify}

.side{position:absolute;left:570px;top:410px;width:312px;height:345px;background:var(--panel)}
.side-photo{position:absolute;left:22px;top:22px;width:270px;height:160px;background:linear-gradient(135deg,#c9c2b8,#8a7f72 60%,#5c5650)}
.news{position:absolute;left:22px;top:194px;width:270px}
.section-title{font-size:25px;font-weight:500;color:var(--orange);margin-bottom:6px}
.blurb{font-size:14px;line-height:1.35;color:var(--muted)}

.lower{position:absolute;left:0;top:755px;width:882px;height:255px;background:var(--white);border-top:1px solid var(--rule)}
.interview-photo{position:absolute;left:40px;top:28px;width:190px;height:190px;background:linear-gradient(160deg,#9a9a9a,#5a5a5a)}
.interview{position:absolute;left:250px;top:28px;width:230px}
.events{position:absolute;left:592px;top:28px;width:260px}
.read-more{display:block;margin-top:14px;font-size:14px;font-weight:700;color:var(--charcoal)}
.lower-divider{position:absolute;left:545px;top:20px;width:1px;height:210px;background:var(--rule)}

.signup{position:absolute;left:0;top:1010px;width:882px;height:68px;background:var(--orange);display:flex;align-items:center;justify-content:space-between;padding:0 40px}
.signup-text{font-size:24px;color:var(--white)}
.signup-btn{background:var(--charcoal);color:var(--white);font-size:22px;font-weight:500;padding:10px 28px;border-radius:3px}

.footer{position:absolute;left:0;top:1078px;width:882px;height:94px;background:var(--charcoal);color:var(--white);font-size:17px}
.contact{position:absolute;display:flex;align-items:center;gap:12px}
.contact svg{width:22px;height:22px}
.phone{left:40px;top:16px}
.mail{left:40px;top:56px}
.web{left:570px;top:16px}
.follow{left:570px;top:56px}
.social{display:flex;gap:6px;margin-left:8px}
.social span{width:22px;height:22px;background:#5b5e64;border-radius:2px}

.legal{position:absolute;left:0;top:1172px;width:882px;height:28px;background:var(--charcoal-deep);color:#7d8087;font-size:11px;padding:8px 40px}
</style>
</head>
<body>
<div class="email">
  <header class="topbar">
    <div class="brand"><span class="brand-dot"></span>BuildLedger</div>
  </header>

  <section class="hero">
    <h1 class="hero-title"><span class="accent">Funding</span><br>the <strong>Construction</strong><br>Industrey!</h1>
    <div class="hero-visual">
      <div class="hero-circle"></div>
      <div class="hero-art" role="img" aria-label="Illustration of a house with dollar bills beside it"></div>
    </div>
  </section>

  <section class="spotlight">
    <h2>Spotlight</h2>
    <p>We provide the trade credit that gives contractors a repayment term of up to 150 days while covering the costs of their supply expenses in 10 days or less. This not only helps the contractors, but helps suppliers as well!</p>
    <h2>Spotlight</h2>
    <p>Financial stress and limited business capabilities are destroying construction professionals. By supporting the financial needs of these companies, we're building better, stronger businesses. When business is strong and stable, construction companies can do amazing things. They are the ones who will literally build our future and build better communities for us to be a part of. We're not only building better lives for contractors and their families, but also impacting the population at large through positive economic, functional improvements that our support helps create.</p>
  </section>

  <aside class="side">
    <div class="side-photo" role="img" aria-label="Photo of a construction worker on site"></div>
    <div class="news">
      <h3 class="section-title">News</h3>
      <p class="blurb">Lorem Ipsum is simply dummy text of the printing and typesetting industry. Lorem Ipsum has been the industry's standard dummy text ever since the 1500s</p>
    </div>
  </aside>

  <section class="lower">
    <div class="interview-photo" role="img" aria-label="Portrait photo of the interviewee"></div>
    <div class="interview">
      <h3 class="section-title">Interview</h3>
      <p class="blurb">Lorem Ipsum is simply dummy text of the printing and typesetting industry. Lorem Ipsum has been the industry's standard dummy text ever since the 1500s</p>
      <span class="read-more">Read more.....</span>
    </div>
    <div class="lower-divider"></div>
    <div class="events">
      <h3 class="section-title">Upcoming Events</h3>
      <p class="blurb">Lorem Ipsum is simply dummy text of the printing and typesetting industry. Lorem Ipsum has been the industry's standard dummy text ever since the 1500s</p>
      <span class="read-more">Read more.....</span>
    </div>
  </section>

  <section class="signup">
    <span class="signup-text">Sign Up for Resources and Exclusive Events</span>
    <span class="signup-btn">Sign Me Up!</span>
  </section>

  <footer class="footer">
    <div class="contact phone">
      <svg viewBox="0 0 24 24"><path fill="#fff" d="M6.6 10.8a15 15 0 0 0 6.6 6.6l2.2-2.2c.3-.3.7-.4 1-.2 1.1.4 2.3.6 3.6.6.6 0 1 .4 1 1V20c0 .6-.4 1-1 1A17 17 0 0 1 3 4c0-.6.4-1 1-1h3.5c.6 0 1 .4 1 1 0 1.3.2 2.5.6 3.6.1.3 0 .7-.2 1z"/></svg>
      +1 (800) 555-0142
    </div>
    <div class="contact mail">
      <svg viewBox="0 0 24 24"><rect x="2" y="5" width="20" height="14" rx="2" fill="#fff"/><path d="M3 6l9 7 9-7" stroke="#2b2d31" stroke-width="1.8" fill="none"/></svg>
      hello@buildledger.com
    </div>
    <div class="contact web">
      <svg viewBox="0 0 24 24"><circle cx="12" cy="12" r="9" fill="none" stroke="#fff" stroke-width="1.8"/><path d="M3 12h18M12 3c3 3.5 3 14.5 0 18M12 3c-3 3.5-3 14.5 0 18" stroke="#fff" stroke-width="1.5" fill="none"/></svg>
      www.buildledger.com
    </div>
    <div class="contact follow">
      Follow:
      <div class="social"><span></span><span></span><span></span><span></span><span></span></div>
    </div>
  </footer>
  <div class="legal">Copyright 2024 BuildLedger. All rights reserved.</div>
</div>
</body>
</html>
```